Tender Lantern Letterhead Design Project

We need a letterhead design for a consultancy business based in Australia.

Tender Lantern is a unique business designed to assist with the complex and time consuming nature of selecting contractors, showing them what to do and reviewing quotes when it comes to body corporate and strata maintenance items such as painting, waterproofing, plumbing and electrical.

Target Market(s)

apartment managers

Industry/Entity Type

Business

Requirements
Must have
• must have logo and contact details

Tender Lantern
82 Corvalla Ridge Road
Tarrowin, QLD 4871
Ph 07 5391 2846
Fax 07 5392 8071
Mobile 0438 917204

```html
<!DOCTYPE html>
<html lang="en">
<head>
<meta charset="utf-8">
<title>Tender Lantern Letterhead</title>
<link rel="stylesheet" href="https://fonts.googleapis.com/css2?family=Jost:wght@300;400&display=swap">
<style>
  :root {
    --brand-red: #e31b2a;
    --name-grey: #b4b4b4;
    --text-grey: #8c8c8c;
    --paper: #ffffff;
  }
  * { margin: 0; padding: 0; box-sizing: border-box; }
  html, body {
    width: 848px;
    height: 1200px;
    overflow: hidden;
    background: var(--paper);
  }
  .letterhead {
    position: relative;
    width: 848px;
    height: 1200px;
    overflow: hidden;
    background: var(--paper);
    font-family: "Jost", "Futura", sans-serif;
  }
  .frame-art {
    position: absolute;
    inset: 0;
    display: block;
  }
  .brand {
    position: absolute;
    left: 0;
    right: 0;
    top: 990px;
    text-align: center;
  }
  .brand-name {
    font-size: 46px;
    font-weight: 400;
    color: var(--name-grey);
    letter-spacing: -0.5px;
    line-height: 1;
  }
  .contact {
    position: absolute;
    left: 0;
    right: 0;
    top: 1077px;
    text-align: center;
    font-size: 16.5px;
    font-weight: 300;
    line-height: 19px;
    color: var(--text-grey);
    text-transform: uppercase;
  }
  .contact-name {
    color: var(--brand-red);
    text-transform: none;
    font-weight: 300;
  }
</style>
</head>
<body>
  <main class="letterhead">
    <svg class="frame-art" width="848" height="1200" viewBox="0 0 848 1200"
         role="img" aria-label="Broad red border framing the writing area of the page">
      <rect x="0" y="0" width="848" height="1200" fill="var(--brand-red)"/>
      <rect x="0" y="0" width="848" height="90" fill="var(--paper)"/>
      <rect x="16" y="228" width="816" height="1020" rx="120" ry="120" fill="var(--paper)"/>
    </svg>

    <header class="brand">
      <div class="brand-name">Tender Lantern</div>
    </header>

    <footer class="contact">
      <p><span class="contact-name">Tender Lantern</span> 82 Corvalla Ridge Road. Tarrowin, QLD 4871</p>
      <p>Ph 07 5391 2846. Fax 07 5392 8071. Mobile 0438 917204</p>
    </footer>
  </main>
</body>
</html>
```